Book cover for a sci fi book called The Velvet Assembly

Dear Pixel Harbor team,

I would need a book cover design for my sci fi book, 'The Velvet Assembly'.

I will start by briefing you about the book's content, then I would like to advice you about a few possible book cover scenarios that I could imagine having for the book, and on which I would like to ask you to work on.

Book abstract:

The velvet assembly is a technically developed and spiritually evolved society from a distant galaxy.

Main location the actions take place: Planet Earth, globalized world, former Northern Germany, a new isolated high tech city at the sea, called Lees, inhabitants from everywhere, one government, one religion.
• Year: 2093
• The Velvet Assembly: solar system with 7 suns. The inhabitans of the velvet assembly have no physical body, only energetical bodies. Only when visiting Earth, they can incarnate at will.

The action starts on planet Earth, where a group of 4 people, two women and two males, who meet through different circumstances and decide to follow together a spiritual and philiosophical path towards self development and evolution. They meet an incarnated master from the velvet assembly who leads their path. At the end of the books, they reach a form of enlightment and transcende to The Velvet Assembly, they only come to know at the end the truth about the real origin of their master.

For the book cover, no matter what ideas you choose, please use max three predominant colors for that, red, yellow and orange. The book cover should inspire warmth.

Suggestions for the design:
- an abstract sun
- a cosmic view of the velvet assembly
- an abstractized design of a sacred geometry shape
- sun in the upper left corner, shining with visible rays on the whole surface of the book cover, a group of 4 people with the female old master sitting by their side in the lower right corner
- an out of the box Ufo, please choose for example an asymmetrical shape, definately not the usual flying sorcer, departing from the velvet assembly solar system, cosmic view from above
- PLEASE FEEL FREE TO BRAINSTROM ON YOUR OWN IDEAS BASED ON WHAT THE BOOK ABSTRACT INSPIRED YOU

For any questions, I am atbyour disposal.

I am looking forward to your design, thank you in advance for that.

Kind regards,
Mira

Target Market(s)

Sci Fi enthusiasts
Philosophers

Font styles to use
Serif

Colors
fbee3e
ffc214
faa54b
f37122
f04a50

Requirements
Must have
• For the book cover, no matter what ideas you choose, please use max three predominant colors for that, red, yellow and orange and/or any derived hues. The book cover should inspire warmth.
• Suggestions for the design:
• - an abstract sun
• - a cosmic view of the velvet assembly
• - an abstractized design of a sacred geometry shape
• - sun in the upper left corner, shining with visible rays on the whole surface of the book cover, a group of 4 people with the female old master sitting by their side in the lower right corner
• - an out of the box Ufo, please choose for example an asymmetrical shape, definately not the usual flying sorcer, departing from the velvet assembly solar system, cosmic view from above
• - PLEASE FEEL FREE TO BRAINSTROM ON YOUR OWN IDEAS BASED ON WHAT THE BOOK ABSTRACT INSPIRED YOU
Nice to have
• Minimalistic and modern design
Should not have
• dark or grey shades
• phtographs

```html
<!DOCTYPE html>
<html lang="en">
<head>
<meta charset="UTF-8">
<title>The Velvet Assembly — Book Cover</title>
<link rel="stylesheet" href="https://fonts.googleapis.com/css2?family=Abril+Fatface&display=swap">
<style>
  :root {
    --page-bg: #f4f4f4;
    --yellow: #fbee3e;
    --amber: #ffc214;
    --orange-light: #faa54b;
    --orange: #f37122;
    --red-orange: #f5400c;
    --red: #f22a06;
    --ink: #121010;
    --ground: #171311;
  }

  * { margin: 0; padding: 0; box-sizing: border-box; }

  html, body {
    width: 1200px;
    height: 1200px;
    overflow: hidden;
    background: var(--page-bg);
  }

  .stage {
    position: relative;
    width: 1200px;
    height: 1200px;
  }

  .book-cover {
    position: absolute;
    left: 256px;
    top: 110px;
    width: 688px;
    height: 980px;
    overflow: hidden;
  }

  .cover-art {
    position: absolute;
    inset: 0;
    background: linear-gradient(205deg, var(--yellow) 0%, var(--amber) 20%, var(--orange-light) 42%, var(--orange) 62%, var(--red-orange) 80%, var(--red) 100%);
  }

  .horizon-scene {
    position: absolute;
    left: 0;
    right: 0;
    bottom: 0;
    height: 66px;
    background: var(--ground);
  }

  .title {
    position: absolute;
    inset: 0;
    font-family: "Abril Fatface", "Bodoni Moda", serif;
    font-weight: 400;
    color: var(--ink);
    text-transform: uppercase;
    line-height: 1;
  }

  .title span {
    position: absolute;
    left: 0;
    right: 0;
    text-align: center;
    white-space: nowrap;
  }

  .title-article {
    top: 410px;
    font-size: 52px;
    letter-spacing: 3px;
  }

  .title-main {
    top: 440px;
    font-size: 140px;
    letter-spacing: 4px;
  }

  .title-sub {
    top: 562px;
    font-size: 108px;
    letter-spacing: 3px;
  }
</style>
</head>
<body>
  <main class="stage">
    <section class="book-cover" aria-label="Book cover: The Velvet Assembly">
      <div class="cover-art" role="img" aria-label="Warm sky with a glowing sun rising over the curved edge of a planet"></div>

      <div class="horizon-scene" role="img" aria-label="Dark horizon with four people seated together, seen in silhouette"></div>

      <h1 class="title">
        <span class="title-article">The</span>
        <span class="title-main">Velvet</span>
        <span class="title-sub">Assembly</span>
      </h1>
    </section>
  </main>
</body>
</html>
```